ready mix concrete business

i need a logo for a ready mix company
it is called Pine Hollow Concrete for business cards and promotional items. would like a ready mix truck on it
and must look profesional

```html
<!DOCTYPE html>
<html lang="en">
<head>
<meta charset="UTF-8">
<title>Pine Hollow Concrete – Business Card</title>
<link href="https://fonts.googleapis.com/css2?family=Exo+2:wght@400;500;700&display=swap" rel="stylesheet">
<style>
  :root {
    --page-bg: #f2f2f2;
    --card-light: #e7eaee;
    --card-grey: #a9acb1;
    --brand-blue: #1f6fc4;
    --white: #ffffff;
    --ink-dark: #2f3238;
  }
  * { box-sizing: border-box; margin: 0; padding: 0; }
  html, body {
    width: 1200px;
    height: 826px;
    overflow: hidden;
    background: var(--page-bg);
    font-family: "Exo 2", sans-serif;
  }
  .canvas {
    position: relative;
    width: 1200px;
    height: 826px;
  }
  .business-card {
    position: absolute;
    left: 100px;
    top: 128px;
    width: 1000px;
    height: 570px;
    background: var(--card-light);
    overflow: hidden;
    box-shadow: 0 6px 24px rgba(0,0,0,0.18);
  }
  .lower-band {
    position: absolute;
    left: 0;
    top: 310px;
    width: 100%;
    height: 260px;
    background: var(--card-grey);
    border-top: 6px solid var(--brand-blue);
  }
  .brand-mark {
    position: absolute;
    left: 0;
    top: 150px;
    width: 100%;
    display: flex;
    justify-content: center;
    align-items: center;
    gap: 18px;
  }
  .brand-dot {
    width: 34px;
    height: 34px;
    border-radius: 50%;
    background: var(--brand-blue);
  }
  .brand-name {
    font-size: 58px;
    font-weight: 700;
    color: var(--brand-blue);
    text-transform: uppercase;
    letter-spacing: 1px;
  }
  .contact-list {
    position: absolute;
    left: 700px;
    top: 340px;
    list-style: none;
    color: var(--white);
    font-size: 19px;
  }
  .contact-list li {
    display: flex;
    align-items: center;
    gap: 14px;
    height: 30px;
  }
  .contact-icon {
    width: 22px;
    height: 22px;
    flex: none;
  }
  .person {
    position: absolute;
    left: 60px;
    top: 410px;
    display: flex;
    align-items: center;
    gap: 22px;
  }
  .avatar {
    width: 84px;
    height: 84px;
    border-radius: 50%;
    border: 5px solid var(--white);
    display: flex;
    align-items: center;
    justify-content: center;
  }
  .person-name {
    color: var(--white);
    font-size: 30px;
    font-weight: 500;
    text-transform: uppercase;
    line-height: 1;
  }
  .person-role {
    color: var(--ink-dark);
    font-size: 18px;
    margin-top: 4px;
  }
  .web-bar {
    position: absolute;
    left: 390px;
    bottom: 0;
    width: 610px;
    height: 72px;
    background: var(--brand-blue);
    border-radius: 36px 0 0 36px;
    display: flex;
    align-items: center;
    justify-content: center;
    color: var(--white);
    font-size: 28px;
    letter-spacing: 1px;
  }
</style>
</head>
<body>
<div class="canvas">
  <div class="business-card">
    <div class="lower-band"></div>

    <div class="brand-mark">
      <span class="brand-dot"></span>
      <span class="brand-name">Pine Hollow Concrete</span>
    </div>

    <ul class="contact-list">
      <li>
        <svg class="contact-icon" viewBox="0 0 24 24"><circle cx="12" cy="12" r="11" fill="#1f6fc4"/><path d="M8 6.5l2 2-1.2 1.6a7 7 0 0 0 5.1 5.1l1.6-1.2 2 2-1.5 1.5c-4.6-.4-8.4-4.2-8.8-8.8z" fill="#fff"/></svg>
        123 456 7890
      </li>
      <li>
        <svg class="contact-icon" viewBox="0 0 24 24"><circle cx="12" cy="12" r="11" fill="#1f6fc4"/><rect x="8.5" y="5.5" width="7" height="13" rx="1.5" fill="#fff"/><rect x="10" y="7.5" width="4" height="8" fill="#1f6fc4"/></svg>
        123 456 7890
      </li>
      <li>
        <svg class="contact-icon" viewBox="0 0 24 24"><circle cx="12" cy="12" r="11" fill="#1f6fc4"/><rect x="6" y="8" width="12" height="8.5" rx="1" fill="#fff"/><path d="M6.5 8.5l5.5 4.5 5.5-4.5" fill="none" stroke="#1f6fc4" stroke-width="1.4"/></svg>
        youremail@gmail.com
      </li>
      <li>
        <svg class="contact-icon" viewBox="0 0 24 24"><circle cx="12" cy="12" r="11" fill="#1f6fc4"/><path d="M12 5a4.5 4.5 0 0 0-4.5 4.5c0 3.4 4.5 8.5 4.5 8.5s4.5-5.1 4.5-8.5A4.5 4.5 0 0 0 12 5z" fill="#fff"/><circle cx="12" cy="9.5" r="1.7" fill="#1f6fc4"/></svg>
        1234 Street Name, Area
      </li>
    </ul>

    <div class="person">
      <div class="avatar">
        <svg width="44" height="46" viewBox="0 0 44 46"><circle cx="22" cy="13" r="10" fill="#fff"/><path d="M2 46c0-12 9-19 20-19s20 7 20 19z" fill="#fff"/></svg>
      </div>
      <div>
        <p class="person-name">Your Name</p>
        <p class="person-role">Post</p>
      </div>
    </div>

    <div class="web-bar">yourwebsite.com</div>
  </div>
</div>
</body>
</html>
```